Letterhead Design Project

I need a simple, clean and corporate letterhead & follow-on letterhead.
The follow-on letterhead should just have the logo only.
Final File Specs:
Full Bleed Size (starting document size)
213 x 300 mm
2517 x 3544 pixels
* Finished artwork should use the full bleed dimensions for best results.
Document Trim Size (final size after being cut)
210 x 297 mm
2480 x 3508 pixels
* Please be sure to keep all text within the safe margin.
Resolution 300 DPI
Accepted file types:-
Adobe Acrobat 9 Document (*.pdf) (recommended)
Adobe Illustrator CS3 Artwork (*.ai) (recommended)
Adobe Photoshop CS3 Image (*.psd) (recommended)
Bitmap Image (*.bmp)
GIF Image (*.gif)
JPEG Image (*.jpg,*.jpeg)
Microsoft PowerPoint 2010 Document (*.ppt)
Microsoft Publisher 2010 Document (*.pub)
Microsoft Word 2010 Document (*.doc)
PCX Image (*.pcx)
PICT Image (*.pic,*.pict,*.pct)
PNG Image (*.png)
PostScript Document (*.ps)
TIF Image (*.tif,*.tiff)
Windows Enhanced Metafile (*.emf)
Windows Metafile (*.wmf)
Requirements
Must have
- My letterhead must have:-
- Logo
- ACN - 418 572 906
- address - Suite 8, 19 Heron St, Maroubra, NSW 2035
- phone - (02) 9361 4258
- fax - (02) 9517 3046
- email - info@brimtarsafety.com.au
- web - www.brimtarsafety.com.au
Follow-on letterhead should have the logo only

```html
<!DOCTYPE html>
<html lang="en">
<head>
<meta charset="utf-8">
<title>Brimtar Asbestos &amp; Safety – Letterhead and Follow-on</title>
<link href="https://fonts.googleapis.com/css2?family=Lato:wght@400;700;900&display=swap" rel="stylesheet">
<style>
  :root {
    --navy: #13122f;
    --green: #8dc63f;
    --paper: #ffffff;
    --backdrop: #f3f3f3;
    --ink: #1d1c3a;
  }
  * { box-sizing: border-box; margin: 0; padding: 0; }
  html, body {
    width: 1200px; height: 900px; overflow: hidden;
    background: var(--backdrop);
    font-family: "Lato", Arial, sans-serif;
    color: var(--ink);
  }
  .stationery {
    position: relative; width: 1200px; height: 900px;
    display: flex; justify-content: center; align-items: center; gap: 40px;
  }
  .sheet {
    position: relative; width: 560px; height: 792px;
    background: var(--paper);
    box-shadow: 0 0 0 1px #e2e2e2;
  }
  .brand {
    position: absolute; left: 52px; top: 60px;
    display: flex; align-items: center; gap: 12px;
  }
  .brand-square {
    width: 34px; height: 34px; border-radius: 5px; background: var(--green);
  }
  .brand-name {
    font-weight: 900; font-size: 22px; color: var(--navy);
    letter-spacing: 0.3px; line-height: 1;
  }
  .contact {
    position: absolute; left: 0; right: 0; bottom: 52px;
    text-align: center; font-size: 10.5px; line-height: 18px; color: var(--ink);
  }
  .contact-row { display: flex; justify-content: center; align-items: center; gap: 12px; }
  .contact-item { display: inline-flex; align-items: center; gap: 4px; }
  .contact-item svg { width: 9px; height: 9px; fill: var(--green); }
  .acn-label { color: var(--green); }
  .footer-band {
    position: absolute; left: 0; right: 0; bottom: 17px; height: 31px;
    background: var(--navy);
    display: flex; align-items: center; justify-content: center;
  }
  .web { color: var(--green); font-size: 10.5px; }
  .footer-square {
    position: absolute; right: 36px; bottom: 8px;
    width: 52px; height: 52px; border-radius: 7px;
    background: var(--paper); border: 5px solid var(--navy);
  }
</style>
</head>
<body>
<main class="stationery">

  <section class="sheet letterhead" aria-label="Letterhead">
    <div class="brand">
      <span class="brand-square"></span>
      <span class="brand-name">Brimtar Asbestos &amp; Safety</span>
    </div>

    <address class="contact">
      <div class="contact-row">
        <span class="contact-item">
          <svg viewBox="0 0 10 10" aria-hidden="true"><path d="M5 0.5 0.5 4.5H2V9.5H4V6.5H6V9.5H8V4.5H9.5Z"/></svg>
          Suite 8, 19 Heron St, Maroubra, NSW 2035
        </span>
      </div>
      <div class="contact-row">
        <span class="contact-item">
          <svg viewBox="0 0 10 10" aria-hidden="true"><rect width="10" height="10" rx="2"/><path d="M3 2.5 4 4 3.5 5 5 6.5 6 6 7.5 7 6.8 8C4.5 7.8 2.2 5.5 2 3.2Z" fill="#fff"/></svg>
          (02) 9361 4258
        </span>
        <span class="contact-item">
          <svg viewBox="0 0 10 10" aria-hidden="true"><rect x="2.5" y="0.5" width="5" height="3"/><rect x="0.5" y="3.5" width="9" height="4" rx="1"/><rect x="2.5" y="6" width="5" height="3.5" fill="#fff" stroke="#8dc63f"/></svg>
          (02) 9517 3046
        </span>
        <span class="contact-item">
          <svg viewBox="0 0 10 10" aria-hidden="true"><rect y="1.5" width="10" height="7" rx="1"/><path d="M0.5 2 5 5.5 9.5 2" fill="none" stroke="#fff" stroke-width="0.9"/></svg>
          info@brimtarsafety.com.au
        </span>
      </div>
      <div class="contact-row"><span><span class="acn-label">ACN</span> - 418 572 906</span></div>
    </address>

    <div class="footer-band"><span class="web">www.brimtarsafety.com.au</span></div>
    <div class="footer-square"></div>
  </section>

  <section class="sheet follow-on" aria-label="Follow-on letterhead">
    <div class="brand">
      <span class="brand-square"></span>
      <span class="brand-name">Brimtar Asbestos &amp; Safety</span>
    </div>
    <div class="footer-band"></div>
    <div class="footer-square"></div>
  </section>

</main>
</body>
</html>
```